REAL ESTATE MAILBOX DROP FLYER

I am looking for two flyer designs. One for DL and one for A4 size. My company is a boutique real estate agency that offers a full/high quality service at a very low commission rate.

Key Phrases to be included

A4 Design should have a space for some text and a table in the center (outline below)

Target Market(s)

Home Owners

Industry/Entity Type

Real Estate Agent

Colors
0455a3

Requirements
Must have
• Eye Catching
• Bold
• high end feel
• Color pallette should match the logo
• The feel of the brochures must convey a trustworthy, high end service.
• Must be eye catching and easy to read
• Editable file formats must be supplied

```html
<!DOCTYPE html>
<html lang="en">
<head>
<meta charset="utf-8">
<title>Northgate Homes – Mailbox Flyer</title>
<link href="https://fonts.googleapis.com/css2?family=Bebas+Neue&family=Lato:wght@400;700;900&display=swap" rel="stylesheet">
<style>
  :root{
    --brand-blue:#0455a3;
    --deep-blue:#04386f;
    --navy:#1d2c44;
    --amber:#f7ab00;
    --white:#ffffff;
    --ink:#111111;
    --stage:#3b3c3b;
  }
  *{box-sizing:border-box;margin:0;padding:0}
  html,body{width:1200px;height:1200px;overflow:hidden;background:var(--stage)}
  body{position:relative;font-family:'Lato',sans-serif}
  .flyer{
    position:absolute;left:234px;top:80px;width:940px;height:1320px;
    transform:scale(0.8);transform-origin:0 0;background:var(--white);overflow:hidden;
  }
  .hero-photo{
    position:absolute;left:0;top:0;width:940px;height:698px;
    background:
      linear-gradient(120deg,rgba(255,255,255,.95) 0%,rgba(255,255,255,.55) 22%,rgba(255,255,255,0) 40%),
      linear-gradient(180deg,#9cc3ea 0%,#c9dcef 22%,#e8ecef 38%,#d9dcd8 48%,#5f8d3a 60%,#4f8f2a 80%,#5a9c2e 100%);
  }
  .brand{
    position:absolute;left:42px;top:82px;display:flex;align-items:center;gap:12px;
    color:var(--navy);font-weight:400;font-size:34px;letter-spacing:1px;line-height:1;
  }
  .brand-mark{width:22px;height:22px;background:var(--navy)}
  .pitch{
    position:absolute;left:30px;top:430px;width:409px;height:515px;background:var(--brand-blue);color:var(--white);
  }
  .pitch-headline{
    position:absolute;left:28px;top:38px;font-family:'Bebas Neue',sans-serif;font-size:84px;line-height:84px;letter-spacing:.5px;
    white-space:nowrap;
  }
  .pitch-rule{position:absolute;left:13px;top:207px;width:373px;height:5px;background:var(--amber)}
  .pitch-rate{
    position:absolute;left:12px;top:222px;font-family:'Bebas Neue',sans-serif;font-size:84px;line-height:1;
    white-space:nowrap;transform:scaleX(.9);transform-origin:0 0;
  }
  .pitch-contact{position:absolute;left:18px;top:303px;font-size:31px;line-height:41px;white-space:nowrap}
  .pitch-contact .phone{color:var(--amber);font-weight:900;font-size:36px}
  .pitch-contact .offer{font-weight:700;font-size:28px;line-height:34px;display:block}
  .pitch-band{
    position:absolute;left:0;bottom:0;width:100%;height:96px;background:var(--deep-blue);
    padding:8px 16px;font-weight:700;font-size:36px;line-height:37px;
  }
  .info-panel{
    position:absolute;left:451px;top:545px;width:462px;height:410px;background:var(--amber);color:var(--white);
  }
  .info-intro{position:absolute;left:28px;top:22px;width:420px;font-size:17px;line-height:20px}
  .table-title{
    position:absolute;left:20px;top:94px;width:420px;display:flex;align-items:center;gap:8px;
    font-size:36px;font-weight:700;
  }
  .table-title::before,.table-title::after{content:"";flex:1;height:3px;background:var(--white)}
  .rates-table{position:absolute;left:20px;top:140px;width:440px;border-collapse:collapse;font-size:15.5px}
  .rates-table th{font-size:19px;font-weight:700;text-align:left;padding:0 0 8px;height:36px}
  .rates-table td{height:25.5px;padding:0;white-space:nowrap}
  .rates-table .col-property{width:126px;padding-left:12px}
  .rates-table .col-amount{width:148px;padding-left:20px;border-left:2px solid var(--white)}
  .rates-table .col-features{padding-left:8px;border-left:2px solid var(--white)}
  .rates-table th.col-amount,.rates-table th.col-features{padding-left:22px}
  .rates-table th.col-property{padding-left:14px}
  .gallery-photo{position:absolute;top:958px;height:176px}
  .gallery-living{left:32px;width:282px;background:linear-gradient(180deg,#e9ebeb 0%,#c9c6c0 55%,#a8a49c 100%)}
  .gallery-bedroom{left:336px;width:274px;background:linear-gradient(180deg,#eef0f1 0%,#d5d4d2 55%,#5d5f63 100%)}
  .gallery-open{left:635px;width:278px;background:linear-gradient(180deg,#e8eaec 0%,#c7c5c2 55%,#9c7d5c 100%)}
  .agent-details{
    position:absolute;left:20px;top:1180px;width:285px;text-align:right;color:var(--ink);font-size:15.5px;line-height:21.5px;font-style:normal;
  }
  .agent-details strong{font-size:19px;font-weight:700;display:block;line-height:26px}
  .agent-portrait{
    position:absolute;left:324px;top:1150px;width:109px;height:140px;border:8px solid var(--ink);background:#777;
  }
  .closing-panel{
    position:absolute;left:451px;top:1150px;width:462px;height:140px;background:var(--amber);color:var(--white);
    padding:10px 26px;font-size:17px;line-height:20px;
  }
  .closing-panel p+p{margin-top:12px}
  .footer-bar{position:absolute;left:0;bottom:0;width:100%;height:13px;background:var(--brand-blue)}
</style>
</head>
<body>
<main class="flyer">
  <div class="hero-photo" role="img" aria-label="Photo of a white weatherboard family home with a steep gabled roof and a freshly mown striped lawn under blue sky"></div>

  <div class="brand"><span class="brand-mark"></span><span>NORTHGATE HOMES</span></div>

  <section class="pitch">
    <h1 class="pitch-headline">Full Service<br>Agency</h1>
    <div class="pitch-rule"></div>
    <p class="pitch-rate">1% Commission</p>
    <p class="pitch-contact">Contact Marcus today on<br><span class="phone">0400 123 456</span> for a<span class="offer">FREE APPRAISAL!</span></p>
    <p class="pitch-band">Save Thousands On<br>Commissions!</p>
  </section>

  <section class="info-panel">
    <p class="info-intro">Lorem ipsum is placeholder text commonly used in the graphic, print, and publishing industries for previewing layouts and visual mockups.</p>
    <h2 class="table-title">Table</h2>
    <table class="rates-table">
      <thead><tr><th class="col-property">Property</th><th class="col-amount">Amount</th><th class="col-features">Features</th></tr></thead>
      <tbody>
        <tr><td class="col-property">Lorem ipsum</td><td class="col-amount">$50,000</td><td class="col-features">consectetur adipiscing</td></tr>
        <tr><td class="col-property">Lorem ipsum</td><td class="col-amount">$50,000</td><td class="col-features">consectetur adipiscing</td></tr>
        <tr><td class="col-property">Lorem ipsum</td><td class="col-amount">$50,000</td><td class="col-features">consectetur adipiscing</td></tr>
        <tr><td class="col-property">Lorem ipsum</td><td class="col-amount">$50,000</td><td class="col-features">consectetur adipiscing</td></tr>
        <tr><td class="col-property">Lorem ipsum</td><td class="col-amount">$50,000</td><td class="col-features">consectetur adipiscing</td></tr>
        <tr><td class="col-property">Lorem ipsum</td><td class="col-amount">$50,000</td><td class="col-features">consectetur adipiscing</td></tr>
        <tr><td class="col-property">Lorem ipsum</td><td class="col-amount">$50,000</td><td class="col-features">consectetur adipiscing</td></tr>
        <tr><td class="col-property">Lorem ipsum</td><td class="col-amount">$50,000</td><td class="col-features">consectetur adipiscing</td></tr>
        <tr><td class="col-property">Lorem ipsum</td><td class="col-amount">$50,000</td><td class="col-features">consectetur adipiscing</td></tr>
      </tbody>
    </table>
  </section>

  <div class="gallery-photo gallery-living" role="img" aria-label="Interior photo of a bright living room with grey sofas and a dining table"></div>
  <div class="gallery-photo gallery-bedroom" role="img" aria-label="Interior photo of a bedroom with a made bed and grey carpet"></div>
  <div class="gallery-photo gallery-open" role="img" aria-label="Interior photo of an open-plan kitchen and lounge with timber floors"></div>

  <address class="agent-details">
    <strong>More Money in YOUR Pocket!</strong>
    Marcus Bell - 0400 123 456<br>
    marcus@northgatehomes.com.au<br>
    www.northgatehomes.com.au
  </address>
  <div class="agent-portrait" role="img" aria-label="Agent portrait placeholder"></div>

  <section class="closing-panel">
    <p>Lorem ipsum is placeholder text commonly used in the graphic, print, and publishing industries for previewing layouts and visual mockups.</p>
    <p>Lorem ipsum is placeholder text commonly used in the graphic, print, and publishing industries for previewing</p>
  </section>

  <div class="footer-bar"></div>
</main>
</body>
</html>
```